Dental specialist needs a sharp looking letterhead

I am looking for a letterhead to be used to send letters and communication between myself (a dental specialist) and other dentists.
My office is a state of the art dental specialty office.
I need to letterhead to also state:
Derek L. Halvorsen DDS
2847 Birchmont Avenue, Suite K
West Larkdale, NY 14390
(716)555-0193
fax: (716)555-0157
halvorsenpulp.com (**this email address may change)

i included my logo designs.
thank you

Target Market(s)

dentists

Industry/Entity Type

Communication

Requirements
Must have
• the included logo, whether the vertical or horizontal versions

```html
<!DOCTYPE html>
<html lang="en">
<head>
<meta charset="utf-8">
<title>Northgate Endodontics P.C. – Letterhead</title>
<link rel="stylesheet" href="https://fonts.googleapis.com/css2?family=Merriweather:wght@300;400&display=swap">
<style>
  :root {
    --paper: #ffffff;
    --ink: #111111;
    --accent-green: #7cc242;
    --accent-blue: #1aa3e8;
    --rule: #8a8a8a;
    --shadow: rgba(0, 0, 0, 0.35);
  }
  html, body {
    margin: 0;
    padding: 0;
    overflow: hidden;
    background: var(--paper);
  }
  .letterhead {
    position: relative;
    width: 851px;
    height: 1200px;
    background: var(--paper);
    overflow: hidden;
    font-family: "Merriweather", Georgia, serif;
  }
  .brand {
    position: absolute;
    left: 30px;
    top: 82px;
    display: flex;
    align-items: center;
    gap: 16px;
  }
  .brand-mark {
    width: 34px;
    height: 34px;
    border-radius: 50%;
    background: var(--accent-blue);
    flex: none;
  }
  .brand-name {
    font-family: "Merriweather", Georgia, serif;
    font-weight: 400;
    font-size: 30px;
    letter-spacing: 0.5px;
    color: var(--ink);
    margin: 0;
    line-height: 1;
  }
  .contact {
    position: absolute;
    left: 583px;
    top: 36px;
    margin: 0;
    font-style: normal;
    font-weight: 300;
    font-size: 18.5px;
    line-height: 22.5px;
    color: var(--ink);
    letter-spacing: -0.4px;
    text-shadow: 2px 3px 4px var(--shadow);
  }
  .contact span { display: block; white-space: nowrap; }
  .contact .doctor {
    color: var(--accent-green);
    font-size: 22px;
    line-height: 30px;
    text-shadow: none;
  }
  .contact .fax { padding-left: 2px; }
  .contact .web { color: var(--accent-blue); }
  .header-rule {
    position: absolute;
    left: 27px;
    top: 194px;
    width: 784px;
    height: 1px;
    background: var(--rule);
    box-shadow: 0 1px 2px rgba(0,0,0,0.15);
  }
</style>
</head>
<body>
  <main class="letterhead">
    <header>
      <div class="brand">
        <span class="brand-mark" aria-hidden="true"></span>
        <p class="brand-name">Northgate Endodontics P.C.</p>
      </div>
      <address class="contact">
        <span class="doctor">Derek L. Halvorsen DDS</span>
        <span class="street">2847 Birchmont Avenue, Suite K</span>
        <span class="city">West Larkdale, NY 14390</span>
        <span class="phone">(716)555-0193</span>
        <span class="fax">fax: (716)555-0157</span>
        <span class="web">halvorsenpulp.com</span>
      </address>
      <div class="header-rule"></div>
    </header>
  </main>
</body>
</html>
```